Simple Modern Label for a Coconut oil product

We need a label designed for Organic Coconut oil. We would like the label to convey the gourmet/high quality product. It should be modern and simple and look like an artisinal product. The label will need to contain all the basic label requirements - Independence list, place for nutrition facts, our company logo etc.
The label will ultimately be printed as oil proof, so it will have a glossy appearance.
I have includes some examples that I like and a file with the logo.

Product Container - Wide Mount Clear Glass Jar: 4.75 inches tall (base to the bottom of the lid) and 9.5 in circumference
Label: Can be 1 or 2 separate labels, round, square and rectangle are okay
No larger than 3 inches high and 9 inches long

Target Market(s)

Middle Age home chef

Industry/Entity Type

Product

Requirements
Must have
• - logo (Attached below, I have this in multiple formats, let me know if you need them)
• - 14 FL OZ (414mL)
• - ingredient: organic unrefined whole kernel virgin coconut oil,
• - Manufacturer: XXX Y St., anywhere, CA, 99999
• - Distributed by Meadowfern Naturals, P.O. Box 5521, Oakland, CA 94612 www.MeadowfernNaturals.example
• - Certified Organic by Company Name
• - Product of Sri Lanka
Nice to have
• - Nutrition Facts
Should not have
• Clutter

```html
<!DOCTYPE html>
<html lang="en">
<head>
<meta charset="utf-8">
<title>Meadowfern Naturals – Organic Coconut Oil Label</title>
<link rel="stylesheet" href="https://fonts.googleapis.com/css2?family=Kanit:wght@500&family=Open+Sans:wght@400;600&display=swap">
<style>
  :root {
    --backdrop: #e4e4e4;
    --teal: #12a5b3;
    --teal-deep: #0e93a1;
    --band: #0d4f55;
    --panel: #ffffff;
    --navy: #17365c;
    --ink: #1f1f1f;
    --info-text: #f2fbfc;
    --seal: #1d5a52;
    --seal-tint: #dfeae7;
  }
  * { box-sizing: border-box; margin: 0; padding: 0; }
  html, body {
    width: 927px; height: 1200px; overflow: hidden;
    background: var(--backdrop);
  }
  .canvas { position: relative; width: 927px; height: 1200px; }

  .label {
    position: absolute; left: 22px; top: 453px;
    width: 883px; height: 294px;
    background: linear-gradient(180deg, var(--teal) 0%, var(--teal-deep) 100%);
    box-shadow: 0 4px 10px rgba(0,0,0,.25);
    overflow: hidden;
  }
  .label__pattern {
    position: absolute; inset: 0;
    background: radial-gradient(circle at 20% 50%, rgba(0,70,80,.10), transparent 60%),
                radial-gradient(circle at 80% 40%, rgba(0,70,80,.08), transparent 55%);
  }

  .front-panel {
    position: absolute; left: 132px; top: 30px;
    width: 286px; height: 232px;
    background: var(--panel); border-radius: 14px; overflow: hidden;
  }
  .brand {
    position: absolute; left: 0; right: 0; top: 50px;
    display: flex; align-items: center; justify-content: center; gap: 10px;
  }
  .brand__mark { width: 22px; height: 22px; background: var(--navy); }
  .brand__name {
    font-family: "Kanit", sans-serif; font-weight: 500;
    font-size: 22px; color: var(--navy); letter-spacing: .5px;
  }
  .product-band {
    position: absolute; left: 0; right: 0; top: 120px; height: 45px;
    background: var(--band);
    display: flex; align-items: center; justify-content: center;
  }
  .product-band__title {
    font-family: "Kanit", sans-serif; font-weight: 500;
    font-size: 23px; color: #fff; letter-spacing: .3px;
  }
  .net-content {
    position: absolute; left: 23px; top: 208px;
    font-family: "Open Sans", sans-serif; font-weight: 600;
    font-size: 11px; color: var(--ink);
  }
  .organic-seal { position: absolute; left: 164px; top: 170px; }

  .info {
    position: absolute; left: 468px; top: 30px; width: 170px;
    font-family: "Open Sans", sans-serif; font-size: 9.8px;
    line-height: 1.3; color: var(--info-text); text-align: center;
  }
  .info__block + .info__block { margin-top: 14px; }
  .info__block--maker { margin-top: 26px !important; }
  .info__heading { font-weight: 600; font-size: 10.5px; }
  .info__ingredients { font-size: 11.5px; line-height: 1.2; }
  .info__web { font-size: 9.5px; white-space: nowrap; }

  .nutrition-panel {
    position: absolute; left: 644px; top: 19px;
    width: 191px; height: 254px; background: #fff;
    padding: 6px 0 0 12px;
  }
  .nutrition-panel__title {
    font-family: "Open Sans", sans-serif; font-weight: 400;
    font-size: 23px; color: #111;
  }
</style>
</head>
<body>
<div class="canvas">
  <section class="label">
    <div class="label__pattern" role="img" aria-label="Faint hand-drawn coconut pattern across the label background"></div>

    <div class="front-panel">
      <div class="brand">
        <span class="brand__mark"></span>
        <span class="brand__name">Meadowfern Naturals</span>
      </div>
      <div class="product-band">
        <h1 class="product-band__title">Organic Coconut Oil</h1>
      </div>
      <p class="net-content">14 FL OZ (414mL)</p>
      <svg class="organic-seal" width="100" height="60" viewBox="0 0 100 60" role="img" aria-label="Organic certification seal area">
        <rect x="8" y="10" width="84" height="40" rx="4" transform="rotate(-8 50 30)"
              fill="var(--seal-tint)" stroke="var(--seal)" stroke-width="3"/>
      </svg>
    </div>

    <div class="info">
      <div class="info__block">
        <p class="info__heading">INGREDIENT:</p>
        <p class="info__ingredients">organic unrefined<br>whole kernel<br>virgin coconut oil</p>
      </div>
      <div class="info__block info__block--maker">
        <p>Manufacturer:</p>
        <p>XXX Y St., anywhere,<br>CA, 99999</p>
      </div>
      <div class="info__block">
        <p>Distributed by:</p>
        <p>Meadowfern Naturals<br>P.O. Box 5521, Oakland,<br>CA 94612</p>
        <p class="info__web">www.MeadowfernNaturals.example</p>
      </div>
      <div class="info__block">
        <p>Product of Sri Lanka</p>
      </div>
    </div>

    <div class="nutrition-panel">
      <h2 class="nutrition-panel__title">Nutrition Facts</h2>
    </div>
  </section>
</div>
</body>
</html>
```